business card letterhead envelope
Darren Holcomb Realtors
Project: business card letterhead envelope
business card letterhead envelope - Real Estate
Creative Brief
Professional
Darren Holcomb
Attorney/Broker
2817 W. Larkspur Ave Suite B7 Odessa, TX 79748
Darren@PecosPrairieHouses.com
PecosPrairieHouses.com

```html
<!DOCTYPE html>
<html lang="en">
<head>
<meta charset="utf-8">
<title>Darren Holcomb Realtors – Business Card</title>
<link rel="stylesheet" href="https://fonts.googleapis.com/css2?family=Open+Sans:wght@400;600;700&display=swap">
<style>
  :root {
    --backdrop: #6a6a6a;
    --frame: #8c8c8c;
    --card: #ffffff;
    --ink: #2b2b2b;
    --ink-soft: #3a3a3a;
    --band: #2a2a2a;
    --band-light: #9a9a9a;
    --ghost: #e8e8e8;
    --on-band: #ffffff;
  }
  * { margin: 0; padding: 0; box-sizing: border-box; }
  html, body {
    width: 1200px; height: 751px; overflow: hidden;
    background: var(--backdrop);
    font-family: "Open Sans", Arial, sans-serif;
  }
  .frame {
    position: absolute; left: 84px; top: 84px; width: 1032px; height: 583px;
    background: var(--frame);
  }
  .card {
    position: absolute; left: 101px; top: 101px; width: 998px; height: 547px;
    background: var(--card); overflow: hidden;
  }
  .card svg.shapes { position: absolute; left: 0; top: 0; }
  .brand {
    position: absolute; left: 130px; top: 210px; width: 340px;
    text-align: center; color: var(--ink);
    font-weight: 400; text-transform: uppercase;
  }
  .brand-name { font-size: 34px; letter-spacing: 1px; line-height: 40px; }
  .brand-sub { font-size: 19px; letter-spacing: 6px; line-height: 30px; }
  .holder {
    position: absolute; left: 48px; top: 289px;
    font-size: 27px; color: var(--ink); white-space: nowrap;
  }
  .holder .name { font-weight: 700; }
  .holder .sep { font-weight: 700; margin: 0 6px; }
  .contact {
    position: absolute; left: 48px; top: 340px;
    list-style: none; font-size: 22px; line-height: 34px; color: var(--ink-soft);
  }
  .contact b { font-weight: 700; }
  .web {
    position: absolute; left: 48px; top: 518px;
    font-size: 24px; font-weight: 700; color: var(--on-band);
    line-height: 29px;
  }
</style>
</head>
<body>
  <div class="frame"></div>
  <main class="card">
    <svg class="shapes" width="998" height="547" viewBox="0 0 998 547" aria-hidden="true">
      <circle class="brand-mark" cx="242" cy="110" r="70" fill="none" stroke="var(--ink)" stroke-width="14"/>
      <circle class="ghost-mark" cx="835" cy="396" r="118" fill="none" stroke="var(--ghost)" stroke-width="18"/>
      <polygon class="band-light" points="708,532 998,532 998,547 714,547" fill="var(--band-light)"/>
      <polygon class="band" points="0,518 690,518 703,547 0,547" fill="var(--band)"/>
    </svg>

    <div class="brand">
      <div class="brand-name">Darren Holcomb</div>
      <div class="brand-sub">Realtors</div>
    </div>

    <p class="holder"><span class="name">Darren Holcomb</span><span class="sep">|</span>Attorney/Broker</p>

    <ul class="contact">
      <li><b>P:</b> 432.555.0147</li>
      <li><b>C:</b> 432.555.0193</li>
      <li><b>F:</b> 432.555.0162</li>
      <li><b>E:</b> Darren@PecosPrairieHouses.com</li>
      <li>2817 W. Larkspur Ave Suite B7 Odessa,TX 79748</li>
    </ul>

    <p class="web">www.PecosPrairieHouses.com</p>
  </main>
</body>
</html>
```